Velmora Jewellery 25% off pinwheelr like business card

I need a business card designed, the card will be used to send with sold items from the stores.
Theme is black and gold like the logo and name (see pictures)
Must have the following:

Velmora Jewellery logo front and back (use pictures)

www.velmorajewellery-example.com
shops.bazaarvane.com.au/Velmora-Jewellery
info@velmorajewellery-example.com

Like us on pinwheelr for 25% OFF your next purchase!

FREE shipping worldwide!

```html
<!DOCTYPE html>
<html lang="en">
<head>
<meta charset="utf-8">
<title>Velmora Jewellery – Business Card</title>
<link href="https://fonts.googleapis.com/css2?family=Josefin+Sans:wght@300;400;600&family=Montserrat:wght@800&display=swap" rel="stylesheet">
<style>
  :root {
    --backdrop: #c6e9df;
    --backdrop-deep: #aadccf;
    --card-black: #050505;
    --gold: #c9a24a;
    --gold-light: #e2c47a;
    --chain-dark: #140f08;
    --chain-warm: #6b4a1e;
  }
  * { margin: 0; padding: 0; box-sizing: border-box; }
  html, body {
    width: 1200px;
    height: 856px;
    overflow: hidden;
  }
  body {
    background: radial-gradient(ellipse at 40% 30%, var(--backdrop) 0%, var(--backdrop-deep) 100%);
    font-family: "Josefin Sans", Arial, sans-serif;
    display: flex;
    align-items: center;
    justify-content: center;
    gap: 40px;
  }
  .card {
    position: relative;
    width: 560px;
    height: 320px;
    border-radius: 34px;
    background: var(--card-black);
    color: var(--gold);
    overflow: hidden;
    box-shadow: 0 18px 40px rgba(0, 0, 0, 0.18);
  }

  /* Brand lockup */
  .brand {
    display: flex;
    align-items: center;
    gap: 14px;
  }
  .brand-mark {
    flex: none;
    border: 2px solid var(--gold);
    border-radius: 50%;
  }
  .brand-name {
    font-weight: 300;
    text-transform: uppercase;
    line-height: 1.15;
    color: var(--gold);
    text-align: left;
  }

  /* Front */
  .card-front {
    display: flex;
    flex-direction: column;
    align-items: center;
    justify-content: center;
    text-align: center;
  }
  .shipping-note {
    font-size: 26px;
    font-weight: 300;
    margin-bottom: 12px;
  }
  .card-front .brand { margin-bottom: 14px; }
  .card-front .brand-mark { width: 90px; height: 90px; }
  .card-front .brand-name { font-size: 29px; letter-spacing: 6px; }
  .offer {
    font-size: 22px;
    font-weight: 300;
    line-height: 1.3;
  }
  .offer .network { font-weight: 600; }
  .offer .discount {
    font-family: "Montserrat", Arial, sans-serif;
    font-weight: 800;
    font-size: 25px;
    color: var(--gold-light);
  }

  /* Back */
  .card-back .chain-photo {
    position: absolute;
    left: 0;
    top: 0;
    width: 250px;
    height: 172px;
    background: linear-gradient(135deg, var(--chain-dark) 0%, var(--chain-warm) 45%, var(--chain-dark) 100%);
  }
  .holder-name {
    position: absolute;
    left: 282px;
    top: 62px;
    font-size: 27px;
    font-weight: 300;
  }
  .card-back .brand {
    position: absolute;
    right: 28px;
    top: 116px;
    gap: 10px;
  }
  .card-back .brand-mark { width: 58px; height: 58px; }
  .card-back .brand-name { font-size: 16px; letter-spacing: 3px; }
  .contact {
    position: absolute;
    left: 36px;
    top: 194px;
    list-style: none;
    font-size: 15px;
    font-weight: 400;
    line-height: 1.45;
  }
</style>
</head>
<body>

  <section class="card card-front" aria-label="Card front">
    <p class="shipping-note">FREE shipping worldwide!</p>
    <div class="brand">
      <span class="brand-mark"></span>
      <span class="brand-name">Velmora<br>Jewellery</span>
    </div>
    <p class="offer">Like us on <span class="network">pinwheelr</span> for <span class="discount">25% OFF</span><br>your next purchase!</p>
  </section>

  <section class="card card-back" aria-label="Card back">
    <div class="chain-photo" role="img" aria-label="Photograph of a gold chain necklace with clasp on black"></div>
    <p class="holder-name">Rowan Ashcombe</p>
    <div class="brand">
      <span class="brand-mark"></span>
      <span class="brand-name">Velmora<br>Jewellery</span>
    </div>
    <ul class="contact">
      <li>r_ashcombe@velmorajewellery-example.com</li>
      <li>www.velmorajewellery-example.com</li>
      <li>shops.bazaarvane.com.au/Velmora-Jewellery</li>
      <li>info@velmorajewellery-example.com</li>
    </ul>
  </section>

</body>
</html>
```